Elegant Vetani Kalo Rhum Label Design-

We are creating a Rum Distillery in the paradise island of Bora Bora which is a beautiful and exclusive honeymoon and tourist destination in the South Pacific. Our Rum label needs to reflect the beauty of Bora Bora and French Polynesia.
We would like to see designs that include the image of Mount Otemanu (* the mountain of Bora Bora) with an overwater bungalow in the image with the lagoon. We would like the label to have a turquoise color theme with either silver, white, or gold as the outline of the images. We are also open to some tropical colors as well that represent this paradise. The image needs to represent high quality class. The bottle will be sold mostly to tourist at a premium price.

On the label it needs to have Vetani Kalo Rhum as the main name-
Subheader- Light Rhum
Sub Sub header- Distilled and Bottled in Bora Bora
It needs to have 40% vol and 70cl on the label

Target Market(s)

American tourists in Bora Bora, French Polynesia

Industry/Entity Type

Rum Distillery

Colors
0094D4
00A9DD
6FCCEA
C7EBF8
E9F6FB
00AB8E
00BBA5
67D7C9
C6EFE9
E9F9F6

Requirements
Must have
• The mountain image of Otemanu and an overwater bungalow which is symbolic of Bora Bora.

```html
<!DOCTYPE html>
<html lang="en">
<head>
<meta charset="utf-8">
<title>Vetani Kalo Rhum – Light Rhum Label</title>
<link rel="stylesheet" href="https://fonts.googleapis.com/css2?family=Alegreya+Sans:wght@400;500;700;800&display=swap">
<style>
  :root {
    --paper: #ffffff;
    --sky-top: #3fb6e8;
    --sky-haze: #c4ecf8;
    --horizon: #11cdee;
    --lagoon: #1fc8e6;
    --lagoon-shallow: #35c3dc;
    --band-title: #3bbfd5;
    --band-sub: #2eaab9;
    --band-lower: #5cc6d7;
    --band-foot: #7dcfdb;
    --ink: #ffffff;
  }
  * { margin: 0; padding: 0; box-sizing: border-box; }
  html, body {
    width: 732px;
    height: 1200px;
    overflow: hidden;
    background: var(--paper);
  }
  .label {
    position: relative;
    width: 732px;
    height: 1200px;
    font-family: "Alegreya Sans", sans-serif;
    color: var(--ink);
  }
  .label-shape {
    position: absolute;
    inset: 0;
  }
  .label-text {
    position: absolute;
    left: 0;
    width: 100%;
    text-align: center;
    line-height: 1;
  }
  .brand-name {
    top: 516px;
    font-weight: 800;
    font-size: 84px;
    letter-spacing: 1px;
    line-height: 108px;
  }
  .variety {
    top: 765px;
    font-weight: 700;
    font-size: 50px;
  }
  .origin {
    top: 856px;
    font-weight: 400;
    font-size: 40px;
    line-height: 47px;
  }
  .specs {
    position: absolute;
    top: 1010px;
    left: 192px;
    width: 356px;
    display: flex;
    justify-content: space-between;
    font-weight: 700;
    font-size: 28px;
  }
</style>
</head>
<body>
<div class="label">
  <svg class="label-shape" width="732" height="1200" viewBox="0 0 732 1200">
    <defs>
      <clipPath id="label-outline">
        <path d="M26 300 C80 300 118 262 118 205 C118 150 150 120 180 110 C250 14 482 14 552 110 C582 120 614 150 614 205 C614 262 652 300 706 300 L706 868 C652 868 614 906 614 970 C614 1030 582 1060 552 1070 C482 1186 250 1186 180 1070 C150 1060 118 1030 118 970 C118 906 80 868 26 868 Z"/>
      </clipPath>
      <linearGradient id="scene-tones" x1="0" y1="0" x2="0" y2="1">
        <stop offset="0" stop-color="var(--sky-top)"/>
        <stop offset="0.5" stop-color="var(--sky-haze)"/>
        <stop offset="0.52" stop-color="var(--horizon)"/>
        <stop offset="0.82" stop-color="var(--lagoon)"/>
        <stop offset="1" stop-color="var(--band-title)"/>
      </linearGradient>
      <linearGradient id="lower-tones" x1="0" y1="0" x2="0" y2="1">
        <stop offset="0" stop-color="var(--band-lower)"/>
        <stop offset="1" stop-color="var(--band-foot)"/>
      </linearGradient>
    </defs>
    <g clip-path="url(#label-outline)">
      <rect class="band-title" x="0" y="0" width="732" height="752" fill="var(--band-title)"/>
      <g class="scene-placeholder" role="img" aria-label="Illustration: overwater bungalow with thatched roof on a wooden pier in a turquoise lagoon, Mount Otemanu and palm-lined motu on the horizon under a bright sky">
        <rect x="0" y="0" width="732" height="580" fill="url(#scene-tones)"/>
        <rect x="56" y="60" width="620" height="440" fill="none" stroke="var(--ink)" stroke-width="2" stroke-dasharray="10 8" opacity="0.7"/>
        <line x1="56" y1="60" x2="676" y2="500" stroke="var(--ink)" stroke-width="1.5" opacity="0.35"/>
        <line x1="676" y1="60" x2="56" y2="500" stroke="var(--ink)" stroke-width="1.5" opacity="0.35"/>
      </g>
      <rect class="band-subtitle" x="0" y="750" width="732" height="84" fill="var(--band-sub)"/>
      <rect class="band-lower" x="0" y="834" width="732" height="366" fill="url(#lower-tones)"/>
    </g>
    <path class="inner-frame" fill="none" stroke="var(--ink)" stroke-width="2"
      d="M42 316 C98 314 134 272 134 210 C134 162 160 136 190 126 C260 36 472 36 542 126 C572 136 598 162 598 210 C598 272 634 314 690 316 L690 852 C634 854 598 896 598 958 C598 1006 572 1032 542 1042 C472 1162 260 1162 190 1042 C160 1032 134 1006 134 958 C134 896 98 854 42 852 Z"/>
  </svg>

  <h1 class="label-text brand-name">VETANI KALO<br>RHUM</h1>
  <h2 class="label-text variety">Light Rhum</h2>
  <p class="label-text origin">Distilled and Bottled<br>in Bora Bora</p>
  <div class="specs"><span class="abv">40% VOL</span><span class="volume">70 CL</span></div>
</div>
</body>
</html>
```